Business card design for upmarket Home Technology design and Installation company

Hello designers, we need a great business card designed.
We need it to convey high tech, and also sophistication .
We work with some of the most affluent people in the world building them home technology systems, and A/V entertainment systems.

Services offered include the following:
Design, sales, installation, and maintenance of

*Home Automation systems
*Distributed / Multi-Room Audio and Video
*High Performance Networks & WiFi
* Lighting and Shade Control
*Home cinema
*Security and CCTV Systems

I have included a copy of our logo to use for your design efforts.

Target Market(s)

Upmarket clients with multi million euro villas.

Industry/Entity Type

Home technology

Contact Information for Business Card

NAME: Derek Halloran ADDRESS: Plaza Brisa Local 42, Port Andratx, 07392 PHONE: +34-602-518-794 EMAIL: DHalloran@VELTRAsmarthomes.com WEB: www.veltrasmarthomes.com

Requirements
Must have
• Our Logo, and our tagline

```html
<!DOCTYPE html>
<html lang="en">
<head>
<meta charset="utf-8">
<title>VELTRA Business Card</title>
<link rel="stylesheet" href="https://fonts.googleapis.com/css2?family=Montserrat:wght@400;500;800&display=swap">
<style>
  :root {
    --backdrop: #d0d0d0;
    --card: #ffffff;
    --ink: #231f20;
    --faint: #e6e6e6;
    --shadow: rgba(0,0,0,0.18);
  }
  * { margin: 0; padding: 0; box-sizing: border-box; }
  html, body {
    width: 1200px; height: 1000px; overflow: hidden;
    background: var(--backdrop);
    font-family: "Montserrat", sans-serif;
    color: var(--ink);
  }
  .card {
    position: absolute;
    left: 262px; width: 678px; height: 387px;
    background: var(--card);
    border-radius: 26px;
    box-shadow: 4px 6px 8px var(--shadow);
    overflow: hidden;
  }
  .card--front { top: 71px; }
  .card--back { top: 500px; }

  .brand {
    position: absolute;
    display: flex; align-items: center; gap: 12px;
    font-weight: 500; letter-spacing: 6px;
    color: var(--ink);
  }
  .brand__dot {
    display: block; border-radius: 50%; background: var(--ink);
  }
  .card--front .brand {
    left: 0; right: 0; top: 190px; justify-content: center;
    font-size: 34px;
  }
  .card--front .brand__dot { width: 16px; height: 16px; }

  .front__web {
    position: absolute; left: 0; right: 0; top: 340px;
    text-align: center; font-size: 15px;
  }

  .back__decor {
    position: absolute; left: 316px; top: 12px;
    width: 440px; height: 440px;
  }

  .contact {
    position: absolute; left: 26px; top: 27px;
    list-style: none; font-size: 14.5px; line-height: 22px;
  }

  .card--back .brand {
    right: 28px; top: 136px; font-size: 24px; letter-spacing: 4px; gap: 9px;
  }
  .card--back .brand__dot { width: 11px; height: 11px; }

  .holder__rule {
    position: absolute; left: 24px; top: 244px;
    width: 215px; height: 3px; background: var(--ink);
  }
  .holder__name {
    position: absolute; left: 24px; top: 258px;
    font-weight: 800; font-size: 50px; line-height: 54px;
    text-transform: uppercase; letter-spacing: 0.5px;
  }
</style>
</head>
<body>
  <section class="card card--front">
    <div class="brand"><span class="brand__dot"></span>VELTRA</div>
    <p class="front__web">www.veltrasmarthomes.com</p>
  </section>

  <section class="card card--back">
    <svg class="back__decor" viewBox="0 0 440 440" aria-hidden="true">
      <circle cx="220" cy="220" r="220" fill="var(--faint)"/>
    </svg>
    <ul class="contact">
      <li>Phone: +34-602-518-794</li>
      <li>Email: dhalloran@veltrasmarthomes.com</li>
      <li>Website: www.veltrasmarthomes.com</li>
      <li>Address: Plaza Brisa, Local 42, 07392 Port d'Andratx,</li>
    </ul>
    <div class="brand"><span class="brand__dot"></span>VELTRA</div>
    <div class="holder__rule"></div>
    <h1 class="holder__name">Derek<br>Halloran</h1>
  </section>
</body>
</html>
```